Business card design for sports medicine and athlete care clinic.

We need a bold, solid business card design for our practitioners to stand out. We treat overuse & sports-related injuries and provide post-operative rehabilitation. Our specialisations include chronic conditions, men’s health, nutrition & musculoskeletal disorders (MSDs). All brand collateral in terms of fonts, logo and colour palette to be provided.

Target Market(s)

Athletes (professional and amateur), sportspeople, predominantly male

Industry/Entity Type

Health And Wellness

Contact Information for Business Card

The front of the card should be white with dark blue text the back dark blue with white text. The logo should be top-left. The business name should be horizontal and right of the logo. The tagline should be directly below centred on the back of the card (see top-banner.png and bottom-banner.png)

Font styles to use
Sans Serif

Colors
0355a3
0293ce
3176b5
ffffff
85acd3

Requirements
Nice to have
• Diagonal and/or horizontal line elements between logo and practitioner details and/or bottom corner of card (see slide.png and tag-bg.png).

```html
<!DOCTYPE html>
<html lang="en">
<head>
<meta charset="utf-8">
<title>Peak Stride Clinic – Business Card</title>
<link rel="stylesheet" href="https://fonts.googleapis.com/css2?family=Montserrat:wght@400;500;700;800&display=swap">
<style>
  :root {
    --navy: #1c1d57;
    --sky: #3aa6dd;
    --charcoal: #24282c;
    --white: #ffffff;
    --ground: #2b2b2d;
    --tint: #85acd3;
  }
  * { box-sizing: border-box; margin: 0; padding: 0; }
  html, body { width: 1200px; height: 900px; overflow: hidden; }
  body {
    background: var(--ground);
    font-family: "Montserrat", sans-serif;
    position: relative;
  }
  .card {
    position: absolute;
    left: 280px;
    width: 640px;
    height: 366px;
    border-radius: 22px;
    overflow: hidden;
    box-shadow: 0 14px 30px rgba(0,0,0,.45);
  }
  .card--front { top: 54px; background: var(--white); color: var(--navy); }
  .card--back { top: 480px; background: var(--navy); color: var(--white); }

  /* Brand lockup */
  .brand { position: absolute; display: flex; align-items: center; gap: 16px; }
  .brand__mark { border-radius: 50%; background: var(--sky); flex: none; }
  .brand__name { font-weight: 800; letter-spacing: .3px; white-space: nowrap; }
  .brand__tagline { color: var(--sky); font-weight: 500; white-space: nowrap; }

  .card--front .brand { left: 36px; top: 40px; }
  .card--front .brand__mark { width: 60px; height: 60px; }
  .card--front .brand__name { font-size: 31px; line-height: 1.1; }
  .card--front .brand__tagline { font-size: 15px; margin-top: 4px; }

  /* Divider band */
  .divider { position: absolute; left: 0; right: 0; top: 140px; }
  .divider__dark { height: 9px; background: var(--charcoal); }
  .divider__light { height: 11px; background: var(--sky); margin-top: 5px; }

  /* Practitioner */
  .person { position: absolute; left: 40px; top: 190px; }
  .person__name { font-size: 21px; font-weight: 800; }
  .person__role { font-size: 13px; color: var(--sky); font-weight: 500; margin: 2px 0 12px; }
  .contact { list-style: none; }
  .contact li { display: flex; align-items: center; gap: 10px; font-size: 13px; font-weight: 500; margin-bottom: 7px; }
  .icon {
    width: 20px; height: 20px; border-radius: 50%; background: var(--sky);
    display: inline-flex; align-items: center; justify-content: center; flex: none;
  }
  .icon svg { width: 12px; height: 12px; }

  /* Address */
  .address {
    position: absolute; right: 40px; top: 190px;
    display: flex; gap: 10px; align-items: flex-start;
    font-size: 12.5px; font-weight: 500; line-height: 1.5; text-align: right;
  }

  /* Footer strip */
  .footer { position: absolute; left: 0; right: 0; bottom: 0; height: 42px; }
  .footer svg.footer__shape { position: absolute; inset: 0; width: 100%; height: 100%; }
  .footer__links {
    position: absolute; right: 34px; top: 0; height: 42px;
    display: flex; align-items: center; gap: 10px;
    color: var(--white); font-size: 12.5px; font-weight: 500;
  }
  .footer__links svg { width: 14px; height: 14px; }

  /* Back */
  .card--back .brand { left: 50%; top: 120px; transform: translateX(-50%); }
  .card--back .brand__mark { width: 72px; height: 72px; }
  .card--back .brand__name { font-size: 36px; }
  .card--back .brand__tagline {
    position: absolute; left: 0; right: 0; top: 255px;
    text-align: center; font-size: 20px;
  }
</style>
</head>
<body>

<section class="card card--front" aria-label="Business card front">
  <div class="brand">
    <span class="brand__mark"></span>
    <div>
      <div class="brand__name">Peak Stride Clinic</div>
      <div class="brand__tagline">Sports medicine and athlete care</div>
    </div>
  </div>

  <div class="divider">
    <div class="divider__dark"></div>
    <div class="divider__light"></div>
  </div>

  <div class="person">
    <div class="person__name">Daniel Reeve</div>
    <div class="person__role">Managing Director</div>
    <ul class="contact">
      <li>
        <span class="icon"><svg viewBox="0 0 12 12"><rect x="3" y="1" width="6" height="10" rx="1.2" fill="none" stroke="#fff" stroke-width="1.2"/><circle cx="6" cy="9.2" r=".7" fill="#fff"/></svg></span>
        555-013-2740
      </li>
      <li>
        <span class="icon"><svg viewBox="0 0 12 12"><path d="M3 1.5 L4.8 1.5 L5.5 4 L4.3 5 Q5.2 7 7 7.7 L8 6.5 L10.5 7.2 L10.5 9 Q10.5 10.5 9 10.5 Q2 10 1.5 3 Q1.5 1.5 3 1.5Z" fill="#fff"/></svg></span>
        555-013-2740
      </li>
      <li>
        <span class="icon"><svg viewBox="0 0 12 12"><rect x="1.5" y="3" width="9" height="6.5" rx=".8" fill="none" stroke="#fff" stroke-width="1.1"/><path d="M1.8 3.4 L6 6.6 L10.2 3.4" fill="none" stroke="#fff" stroke-width="1.1"/></svg></span>
        daniel@mailbox.com
      </li>
    </ul>
  </div>

  <div class="address">
    <div>118 Harbour Lane<br>Suite 12, Westbrook<br>MI 49010</div>
    <span class="icon"><svg viewBox="0 0 12 12"><path d="M6 1 Q9.5 1 9.5 4.5 Q9.5 7 6 11 Q2.5 7 2.5 4.5 Q2.5 1 6 1Z" fill="#fff"/><circle cx="6" cy="4.5" r="1.3" fill="#3aa6dd"/></svg></span>
  </div>

  <div class="footer">
    <svg class="footer__shape" viewBox="0 0 640 42" preserveAspectRatio="none">
      <polygon points="250,42 290,0 640,0 640,42" fill="var(--navy)"/>
    </svg>
    <div class="footer__links">
      <span>PeakStrideAU</span>
      <svg viewBox="0 0 14 14"><circle cx="7" cy="7" r="6" fill="none" stroke="#fff" stroke-width="1.2"/><ellipse cx="7" cy="7" rx="2.6" ry="6" fill="none" stroke="#fff" stroke-width="1"/><line x1="1" y1="7" x2="13" y2="7" stroke="#fff" stroke-width="1"/></svg>
      <span>peakstrideclinic.com.au</span>
    </div>
  </div>
</section>

<section class="card card--back" aria-label="Business card back">
  <div class="brand">
    <span class="brand__mark"></span>
    <div class="brand__name">Peak Stride Clinic</div>
  </div>
  <div class="brand__tagline">Sports medicine and athlete care</div>
</section>

</body>
</html>
```